LANTERNHILL Pizza and Wraps

We need a website for a new restaurant called LANTERNHILL "PIZZA AND WRAPS".
I have attached fonts, background images, logo, images, content etc.
can provide you with what you need to get the website design done fast and easy
Updates

I have uploaded more images of the venue and some menu items. let me know if there is anything I need to provide to make your mission clear and easy

Reason: i would like a little time to provide more feedback to designers

Industry/Entity Type

Restaurant

Coding

Coded - Design and coding required

Number of Pages Required

5+ page

Colors

Designer to choose colors to be used in the design.

Requirements
Must have
• PAGES:
• Our Story
• Menu
• Reservations
• Catering & Delivery
• Contact

```html
<!DOCTYPE html>
<html lang="en">
<head>
<meta charset="utf-8">
<title>LANTERNHILL Pizza and Wraps</title>
<link rel="stylesheet" href="https://fonts.googleapis.com/css2?family=Tinos:wght@400;700&display=swap">
<style>
  :root {
    --brick-dark: #5e3a2a;
    --brick-mid: #8a5a40;
    --brick-light: #a97a5c;
    --header-white: #ffffff;
    --nav-veil: rgba(245, 243, 241, 0.93);
    --panel-veil: rgba(245, 243, 241, 0.94);
    --brand-red: #e41b23;
    --nav-active: #1d1d1d;
    --nav-idle: #6b6b6b;
    --photo-warm: #e0a93a;
    --photo-amber: #b7792e;
    --photo-deep: #3a2a1e;
    --arrow: rgba(255, 255, 255, 0.75);
  }
  * { box-sizing: border-box; margin: 0; padding: 0; }
  html, body {
    width: 1085px;
    height: 1200px;
    overflow: hidden;
  }
  body {
    position: relative;
    font-family: "Tinos", "Times New Roman", serif;
  }
  .brick-backdrop {
    position: absolute;
    inset: 0;
    background:
      linear-gradient(180deg, rgba(0,0,0,0.08), rgba(0,0,0,0) 40%),
      linear-gradient(115deg, var(--brick-dark) 0%, var(--brick-mid) 35%, var(--brick-light) 60%, var(--brick-mid) 85%, var(--brick-dark) 100%);
  }
  .site-header {
    position: absolute;
    top: 48px;
    left: 0;
    width: 1080px;
    height: 330px;
    background: var(--header-white);
    display: flex;
    flex-direction: column;
    align-items: center;
    justify-content: center;
    gap: 14px;
  }
  .brand-name {
    font-weight: 700;
    font-size: 112px;
    letter-spacing: 2px;
    color: var(--brand-red);
    line-height: 1;
  }
  .brand-tagline {
    font-weight: 700;
    font-size: 34px;
    letter-spacing: 8px;
    color: var(--brand-red);
    line-height: 1;
  }
  .main-nav {
    position: absolute;
    top: 403px;
    left: 0;
    width: 1080px;
    height: 87px;
    background: var(--nav-veil);
  }
  .main-nav ul {
    list-style: none;
    display: flex;
    justify-content: center;
    align-items: center;
    height: 100%;
    white-space: nowrap;
  }
  .main-nav li {
    font-size: 15px;
    letter-spacing: 2px;
    color: var(--nav-idle);
    padding: 0 17px;
  }
  .main-nav li.is-active { color: var(--nav-active); }
  .hero-panel {
    position: absolute;
    top: 515px;
    left: 73px;
    width: 930px;
    height: 700px;
    background: var(--panel-veil);
    padding: 24px;
  }
  .hero-slide {
    position: relative;
    width: 882px;
    height: 680px;
    background:
      linear-gradient(180deg, rgba(0,0,0,0) 55%, rgba(60,40,25,0.35) 100%),
      linear-gradient(90deg, var(--photo-amber) 0%, var(--photo-warm) 35%, var(--photo-warm) 60%, var(--photo-amber) 80%, var(--photo-deep) 100%);
  }
  .slide-arrow {
    position: absolute;
    top: 438px;
    width: 20px;
    height: 24px;
  }
  .slide-arrow--prev { left: 53px; }
  .slide-arrow--next { right: 60px; }
</style>
</head>
<body>
  <div class="brick-backdrop" role="img" aria-label="Exposed red brick wall background"></div>

  <header class="site-header">
    <h1 class="brand-name">LANTERNHILL</h1>
    <p class="brand-tagline">PIZZA AND WRAPS</p>
  </header>

  <nav class="main-nav">
    <ul>
      <li class="is-active">HOME</li>
      <li>OUR STORY</li>
      <li>MENU</li>
      <li>RESERVATIONS</li>
      <li>CATERING &amp; DELIVERY</li>
      <li>EVENTS</li>
      <li>CONTACT</li>
    </ul>
  </nav>

  <section class="hero-panel">
    <div class="hero-slide" role="img" aria-label="Restaurant interior photo: wicker chair and a bucket of fries in front of a window into a warm yellow dining room with brick walls">
      <svg class="slide-arrow slide-arrow--prev" viewBox="0 0 20 24" aria-hidden="true">
        <polyline points="14,4 6,12 14,20" fill="none" stroke="var(--arrow)" stroke-width="4"/>
      </svg>
      <svg class="slide-arrow slide-arrow--next" viewBox="0 0 20 24" aria-hidden="true">
        <polyline points="6,4 14,12 6,20" fill="none" stroke="var(--arrow)" stroke-width="4"/>
      </svg>
    </div>
  </section>
</body>
</html>
```